Bussines Card Maple
MAPLE BARBER SHOP
Project: Bussines Card Maple
Bussines Card Maple - Salon & Spa
Creative Brief
Bright & Fun-filled
418 ELM RD SUITE 1 HOLLOWAY, N.Y. 10555
maplebarbershop@examplemail.com
Concepts
Business Card Design Hair Salon
Stationery Package for Nail Salon
lunarbakehouse lunarbakehouse
Phone number, fax, and info just make it bigger please.
Please only use Maple Barber Shop but use the same colors you've been using. Just discard the logo on the front side but on the back use the logo only. Thank you

```html
<!DOCTYPE html>
<html lang="en">
<head>
<meta charset="utf-8">
<title>Maple Barber Shop – Business Card</title>
<link rel="stylesheet" href="https://fonts.googleapis.com/css2?family=Cinzel:wght@600&family=Oswald:wght@300;400&display=swap">
<style>
  :root{
    --backdrop:#e6e7ea;
    --card-white:#ffffff;
    --sketch-tone:#eef0f4;
    --navy-deep:#020a2c;
    --navy-mid:#0a2070;
    --royal:#1d45c9;
    --ink-white:#ffffff;
    --ink-soft:#dfe6ff;
    --shadow:rgba(10,20,50,.22);
  }
  *{margin:0;padding:0;box-sizing:border-box}
  html,body{width:1200px;height:722px;overflow:hidden;background:var(--backdrop)}
  .canvas{
    position:relative;width:1200px;height:722px;
    display:flex;justify-content:center;align-items:center;gap:80px;
  }
  .card{
    position:relative;width:370px;height:640px;border-radius:20px;overflow:hidden;
    box-shadow:0 14px 34px var(--shadow);
  }
  /* front */
  .card--front{background:var(--card-white)}
  .tool-sketches{
    position:absolute;inset:0;
    background:linear-gradient(160deg,var(--sketch-tone),#f8f9fb 55%,var(--sketch-tone));
  }
  .name-oval{
    position:absolute;left:25px;top:215px;width:320px;height:210px;border-radius:50%;
    background:radial-gradient(ellipse at 65% 35%,var(--royal),var(--navy-mid) 55%,var(--navy-deep));
    display:flex;flex-direction:column;align-items:center;justify-content:center;
  }
  .brand-name{
    font-family:"Cinzel",serif;font-weight:600;color:var(--ink-white);
    text-align:center;line-height:1.15;
  }
  .name-oval .brand-name{font-size:40px;letter-spacing:2px}
  .name-oval .brand-name span{display:block;font-size:15px;letter-spacing:3px}
  .name-oval .est-line{position:static;align-self:flex-end;margin:6px 78px 0 0}
  /* back */
  .card--back{
    background:radial-gradient(ellipse at 80% 12%,var(--royal),var(--navy-mid) 45%,var(--navy-deep) 90%);
  }
  .card--back .brand-name{
    position:absolute;top:78px;left:0;right:0;font-size:46px;letter-spacing:3px;
  }
  .card--back .brand-name span{display:block;font-size:16px;letter-spacing:3.5px;margin-top:4px}
  .est-line{
    position:absolute;top:168px;right:56px;
    font-family:"Oswald",sans-serif;font-weight:300;font-size:11px;letter-spacing:1px;color:var(--ink-soft);
  }
  .contact-list{
    position:absolute;left:36px;right:20px;top:330px;list-style:none;
    font-family:"Oswald",sans-serif;font-weight:300;color:var(--ink-white);
    font-size:17px;letter-spacing:.5px;
  }
  .contact-item{display:flex;align-items:flex-start;gap:14px;margin-bottom:20px;line-height:1.3}
  .contact-icon{
    flex:0 0 24px;width:24px;height:24px;border-radius:50%;background:var(--ink-white);
    display:flex;align-items:center;justify-content:center;
  }
  .contact-icon svg{width:14px;height:14px;fill:var(--navy-mid)}
  .contact-item--email{font-size:15px}
</style>
</head>
<body>
<main class="canvas">
  <section class="card card--front">
    <div class="tool-sketches" role="img" aria-label="Faint line sketches of barber tools: scissors, hair dryer and combs"></div>
    <div class="name-oval">
      <p class="brand-name">MAPLE<span>BARBER SHOP</span></p>
      <p class="est-line">EST. 2016</p>
    </div>
  </section>

  <section class="card card--back">
    <p class="brand-name">MAPLE<span>BARBER SHOP</span></p>
    <p class="est-line">EST. 2016</p>
    <ul class="contact-list">
      <li class="contact-item">
        <span class="contact-icon"><svg viewBox="0 0 24 24"><path d="M6.6 10.8a15.1 15.1 0 0 0 6.6 6.6l2.2-2.2a1 1 0 0 1 1-.25 11.4 11.4 0 0 0 3.6.57 1 1 0 0 1 1 1V20a1 1 0 0 1-1 1A17 17 0 0 1 3 4a1 1 0 0 1 1-1h3.5a1 1 0 0 1 1 1 11.4 11.4 0 0 0 .57 3.6 1 1 0 0 1-.25 1z"/></svg></span>
        845 555 0142
      </li>
      <li class="contact-item">
        <span class="contact-icon"><svg viewBox="0 0 24 24"><path d="M6 3h12v5H6zM4 9h16a2 2 0 0 1 2 2v6h-4v4H6v-4H2v-6a2 2 0 0 1 2-2zm4 7v3h8v-3z"/></svg></span>
        845 555 0178
      </li>
      <li class="contact-item">
        <span class="contact-icon"><svg viewBox="0 0 24 24"><circle cx="12" cy="12" r="6"/></svg></span>
        LUNARBAKEHOUSE
      </li>
      <li class="contact-item contact-item--email">
        <span class="contact-icon"><svg viewBox="0 0 24 24"><path d="M3 5h18v14H3zm2 2v.5l7 5 7-5V7zm0 3v7h14v-7l-7 5z"/></svg></span>
        MAPLEBARBERSHOP@EXAMPLEMAIL.COM
      </li>
      <li class="contact-item">
        <span class="contact-icon"><svg viewBox="0 0 24 24"><path d="M12 2a7 7 0 0 0-7 7c0 5 7 13 7 13s7-8 7-13a7 7 0 0 0-7-7zm0 9.5A2.5 2.5 0 1 1 12 6.5a2.5 2.5 0 0 1 0 5z"/></svg></span>
        <span>418 ELM RD SUITE 1<br>HOLLOWAY, N.Y. 10555</span>
      </li>
    </ul>
  </section>
</main>
</body>
</html>
```